Etiketten-Design für Anbieter von hochwertigen Ergänzungsfuttermitteln für Hunde und Katzen
Zielgruppe
Wir bieten hochwertige Ergänzungsfuttermittel in Lebensmittelqualität in erster Linie für Hunde und Katzen an.
Aufgabenstellung
Wir suchen auf diesem Weg ein besonderes Etiketten-Design, welches universell und einheitlich für unsere verschiedenen Produktarten wie Gelenkkomplex, Vitamin Präparat, Beruhigungstabletten usw. anwendbar ist. Außerdem soll das Design einen hohen Wiedererkennungswert aufweisen.
Das Logo unserer Marke besteht bereits. Dieses können Sie im Anhang sehen. Wie Sie dieses farblich in das Etikett einbinden, bleibt Ihnen überlassen.
Bitte keine freigestellten Hunde oder Katzen in das Etikett einbauen.
Gerne hätten wir auf der Front folgende Angaben abgebildet:
- Firmenlogo
- Name des Produktes, „GELENK KOMPLEX“
- Hinweis mit Icon für welches Tier das Produkt geeignet ist: „Für Hunde jeder Rasse und jeden Alters“
- Hinweis Made in Germany - Flagge bzw Deutschlandfarben dezent reichen aus
- Hinweis zum Inhalt: Mit Grünlippmuschelextrakt, Chondroitin, Teufelskralle, MSM usw.
- Hinweis zu: „Ohne künstliche Zusätze“
Sollte es design- oder platztechnisch nicht möglich sein, alles unterzubringen, kann gegebenenfalls auf die Hinweise zum Inhalt verzichtet werden.
Die Verpackung hat eine Höhe von 10cm und einen Durchmesser von 7,5 cm. Das Etikett wird die gesamte seitliche Fläche der Dose beanspruchen, wodurch man dieses nicht farblich an die Verpackung selbst anpassen muss.

```html
<!DOCTYPE html>
<html lang="de">
<head>
<meta charset="utf-8">
<title>Tierwacht – Etiketten</title>
<link href="https://fonts.googleapis.com/css2?family=Amatic+SC:wght@700&family=Montserrat:wght@400;500;600;800&display=swap" rel="stylesheet">
<style>
  :root {
    --bg-top: #e9e9e9;
    --bg-bottom: #d4d8dd;
    --paper: #ece6dc;
    --paper-edge: #e2d9cb;
    --ink: #2e3336;
    --ink-soft: #4a4f52;
    --green: #3aaa4a;
    --purple: #8e5a8e;
    --blue: #86adc4;
    --paw: #6f7274;
  }
  * { box-sizing: border-box; margin: 0; padding: 0; }
  html, body { width: 740px; height: 1200px; overflow: hidden; }
  body {
    background: linear-gradient(180deg, var(--bg-top) 0%, var(--bg-top) 55%, var(--bg-bottom) 100%);
    font-family: "Montserrat", sans-serif;
    color: var(--ink);
    position: relative;
  }
  .label {
    --u: 1;
    position: absolute;
    width: calc(var(--u) * 480px);
    height: calc(var(--u) * 439px);
    background: radial-gradient(ellipse at 50% 40%, var(--paper) 0%, var(--paper) 55%, var(--paper-edge) 100%);
    overflow: hidden;
  }
  .label--main { left: 130px; top: 60px; }
  .label--vitamine { --u: 0.667; --accent: var(--purple); left: 35px; top: 600px; }
  .label--beruhigung { --u: 0.667; --accent: var(--blue); left: 385px; top: 600px; }
  .label--main { --accent: var(--green); }

  .variant-band {
    position: absolute;
    left: 50%;
    top: 0;
    transform: translateX(-50%);
    width: calc(var(--u) * 42px);
    height: calc(var(--u) * 95px);
    background: var(--accent);
    display: flex; align-items: center; justify-content: center;
  }
  .variant-band span {
    writing-mode: vertical-rl;
    transform: rotate(180deg);
    color: #fff;
    font-weight: 800;
    font-size: calc(var(--u) * 7px);
    letter-spacing: 0.5px;
  }
  .free-badge {
    position: absolute;
    left: calc(var(--u) * 305px);
    top: calc(var(--u) * 28px);
    width: calc(var(--u) * 52px);
    height: calc(var(--u) * 52px);
  }
  .brand {
    position: absolute;
    left: 0; right: 0;
    top: calc(var(--u) * 140px);
    display: flex; align-items: center; justify-content: center;
    gap: calc(var(--u) * 10px);
  }
  .brand-dot {
    width: calc(var(--u) * 22px);
    height: calc(var(--u) * 22px);
    border-radius: 50%;
    background: var(--ink);
  }
  .brand-name {
    font-weight: 800;
    font-size: calc(var(--u) * 40px);
    letter-spacing: calc(var(--u) * 1px);
    color: var(--ink);
  }
  .product-name {
    position: absolute; left: 0; right: 0;
    top: calc(var(--u) * 250px);
    text-align: center;
    font-family: "Amatic SC", sans-serif;
    font-weight: 700;
    font-size: calc(var(--u) * 46px);
    line-height: 1;
    color: var(--ink);
  }
  .product-claim {
    position: absolute; left: 0; right: 0;
    top: calc(var(--u) * 298px);
    text-align: center;
    font-weight: 600;
    font-size: calc(var(--u) * 10px);
    line-height: 1.2;
    color: var(--ink);
  }
  .animal-icon {
    position: absolute;
    left: 50%;
    top: calc(var(--u) * 340px);
    transform: translateX(-50%);
    width: calc(var(--u) * 30px);
    height: calc(var(--u) * 30px);
    border-radius: 50%;
    background: var(--ink);
  }
  .suitability {
    position: absolute; left: 0; right: 0;
    top: calc(var(--u) * 375px);
    text-align: center;
    font-weight: 400;
    font-size: calc(var(--u) * 10px);
    line-height: 1.2;
    color: var(--ink-soft);
  }
  .paw-deco {
    position: absolute;
    left: calc(var(--u) * 310px);
    top: calc(var(--u) * 358px);
    width: calc(var(--u) * 56px);
    height: calc(var(--u) * 42px);
    border-radius: 40%;
    background: radial-gradient(circle, rgba(111,114,116,0.35) 0%, rgba(111,114,116,0) 70%);
  }
  .origin-band {
    position: absolute;
    left: 50%;
    bottom: 0;
    transform: translateX(-50%);
    width: calc(var(--u) * 130px);
    height: calc(var(--u) * 17px);
    background: var(--accent);
    color: #fff;
    font-weight: 600;
    font-size: calc(var(--u) * 7.5px);
    display: flex; align-items: center; justify-content: center;
    letter-spacing: 0.4px;
  }
</style>
</head>
<body>

<section class="label label--main">
  <div class="variant-band"><span>GELENKKOMPLEX</span></div>
  <svg class="free-badge" viewBox="0 0 52 52" aria-label="Ohne künstliche Zusätze">
    <circle cx="26" cy="26" r="24" fill="none" stroke="#3aaa4a" stroke-width="4"/>
    <circle cx="26" cy="26" r="11" fill="#3aaa4a"/>
    <path d="M21 26 l4 4 l7 -8" fill="none" stroke="#fff" stroke-width="2.4" stroke-linecap="round" stroke-linejoin="round"/>
  </svg>
  <div class="brand"><span class="brand-dot"></span><span class="brand-name">TIERWACHT</span></div>
  <h1 class="product-name">GELENKKOMPLEX</h1>
  <p class="product-claim">Mit Grünlippmuschelextrakt, Chondroitin,<br>Teufelskralle, MSM usw.</p>
  <div class="animal-icon" role="img" aria-label="Hunde-Symbol"></div>
  <p class="suitability">Für Hunde jeder Rasse<br>und jeden Alters</p>
  <div class="paw-deco" role="img" aria-label="Pfotenabdrücke"></div>
  <div class="origin-band">· MADE IN GERMANY ·</div>
</section>

<section class="label label--vitamine">
  <div class="variant-band"><span>VITAMINE</span></div>
  <svg class="free-badge" viewBox="0 0 52 52" aria-label="Ohne künstliche Zusätze">
    <circle cx="26" cy="26" r="24" fill="none" stroke="#3aaa4a" stroke-width="4"/>
    <circle cx="26" cy="26" r="11" fill="#3aaa4a"/>
    <path d="M21 26 l4 4 l7 -8" fill="none" stroke="#fff" stroke-width="2.4" stroke-linecap="round" stroke-linejoin="round"/>
  </svg>
  <div class="brand"><span class="brand-dot"></span><span class="brand-name">TIERWACHT</span></div>
  <h2 class="product-name">VITAMINE</h2>
  <p class="product-claim">Vitaminpräparat u.a. mit Vitamin A, B, E</p>
  <div class="animal-icon" role="img" aria-label="Hunde-Symbol"></div>
  <p class="suitability">Für Hunde jeder Rasse<br>und jeden Alters</p>
  <div class="paw-deco" role="img" aria-label="Pfotenabdrücke"></div>
  <div class="origin-band">· MADE IN GERMANY ·</div>
</section>

<section class="label label--beruhigung">
  <div class="variant-band"><span>BERUHIGUNG</span></div>
  <svg class="free-badge" viewBox="0 0 52 52" aria-label="Ohne künstliche Zusätze">
    <circle cx="26" cy="26" r="24" fill="none" stroke="#3aaa4a" stroke-width="4"/>
    <circle cx="26" cy="26" r="11" fill="#3aaa4a"/>
    <path d="M21 26 l4 4 l7 -8" fill="none" stroke="#fff" stroke-width="2.4" stroke-linecap="round" stroke-linejoin="round"/>
  </svg>
  <div class="brand"><span class="brand-dot"></span><span class="brand-name">TIERWACHT</span></div>
  <h2 class="product-name">BERUHIGUNG</h2>
  <p class="product-claim">Präparat zur stärkung der Nerven</p>
  <div class="animal-icon" role="img" aria-label="Hunde-Symbol"></div>
  <p class="suitability">Für Hunde jeder Rasse<br>und jeden Alters</p>
  <div class="paw-deco" role="img" aria-label="Pfotenabdrücke"></div>
  <div class="origin-band">· MADE IN GERMANY ·</div>
</section>

</body>
</html>
```